Bref créative
Fjellbrinken Tannregulering Stationery
Orthodontic Clinic
Professional
Fjellbrinken Tannregulering
Kjeveortoped Stian Haugvik
Myrbakkvegen 128
Postboks 71 Kvernvika
5912 BERGEN
post@smilbrink.no
www.smilbrink.no
Telefon 55 83 17 62

```html
<!DOCTYPE html>
<html lang="no">
<head>
<meta charset="utf-8">
<title>Fjellbrinken Tannregulering – visittkort</title>
<link href="https://fonts.googleapis.com/css2?family=Source+Sans+3:wght@400;600;700&display=swap" rel="stylesheet">
<style>
  :root {
    --page: #ffffff;
    --blue-deep: #1f3f8f;
    --blue-mid: #1a78c8;
    --blue-light: #3fb0e8;
    --green-deep: #4f9a22;
    --green-mid: #7cc142;
    --green-light: #9fd45a;
    --ink-blue: #1b5fae;
    --ink-green: #5fa82c;
    --white: #ffffff;
  }
  * { box-sizing: border-box; margin: 0; padding: 0; }
  html, body { width: 1200px; height: 730px; overflow: hidden; background: var(--page); }
  body { position: relative; font-family: "Source Sans 3", Arial, sans-serif; }

  .card {
    position: absolute;
    width: 547px;
    height: 336px;
    overflow: hidden;
    box-shadow: 0 0 0 1px rgba(0,0,0,0.12);
  }
  .card--front { left: 43px; top: 24px; background: var(--white); }
  .card--back-blue { left: 614px; top: 24px;
    background: linear-gradient(100deg, var(--blue-light) 0%, var(--blue-mid) 45%, var(--blue-deep) 100%); }
  .card--back-green { left: 324px; top: 372px;
    background: radial-gradient(ellipse at 45% 45%, var(--green-light) 0%, var(--green-mid) 45%, var(--green-deep) 100%); }

  .front-shape { position: absolute; inset: 0; }

  .brand {
    position: absolute; left: 0; right: 0; top: 50px;
    display: flex; align-items: center; justify-content: center; gap: 12px;
  }
  .brand__dot { width: 44px; height: 44px; border-radius: 50%; background: var(--ink-blue); }
  .brand__block { display: flex; flex-direction: column; }
  .brand__name { font-weight: 700; font-size: 25px; line-height: 1.05; color: var(--ink-blue); text-transform: uppercase; }
  .brand__sub { font-size: 13px; color: var(--ink-blue); }

  .front-title {
    position: absolute; left: 0; right: 0; top: 146px; text-align: center;
    font-size: 25px; color: var(--ink-blue); line-height: 1;
  }
  .front-role {
    position: absolute; left: 0; right: 0; top: 174px; text-align: center;
    font-size: 17px; color: var(--ink-green); line-height: 1;
  }
  .front-contact {
    position: absolute; left: 0; right: 0; top: 248px; text-align: center;
    font-size: 15px; line-height: 22px; color: var(--white);
  }

  .emblem { position: absolute; left: 50%; transform: translateX(-50%); }
  .card--back-blue .emblem { top: 72px; }
  .card--back-green .emblem { top: 118px; }

  .back-text {
    position: absolute; left: 0; right: 0; text-align: center; color: var(--white);
  }
  .card--back-blue .back-text { top: 234px; font-size: 18px; line-height: 21px; }
  .card--back-green .back-text { top: 270px; font-size: 15px; line-height: 20px; }
</style>
</head>
<body>

<section class="card card--front" aria-label="Visittkort forside">
  <svg class="front-shape" viewBox="0 0 547 336" width="547" height="336" aria-hidden="true">
    <defs>
      <linearGradient id="frontBlue" x1="0" y1="0" x2="1" y2="0">
        <stop offset="0" stop-color="#3fb0e8"/>
        <stop offset="0.5" stop-color="#1a78c8"/>
        <stop offset="1" stop-color="#1f3f8f"/>
      </linearGradient>
    </defs>
    <path d="M0 198 Q273 250 547 150 L547 336 L0 336 Z" fill="#7cc142"/>
    <path d="M0 210 Q273 258 547 164 L547 336 L0 336 Z" fill="url(#frontBlue)"/>
  </svg>

  <div class="brand">
    <span class="brand__dot"></span>
    <div class="brand__block">
      <span class="brand__name">Fjellbrinken<br>Tannregulering</span>
      <span class="brand__sub">Kjeveortoped Stian Haugvik</span>
    </div>
  </div>

  <p class="front-title">Fjellbrinken Tannregulering</p>
  <p class="front-role">Kjeveortoped Stian Haugvik</p>

  <address class="front-contact" style="font-style:normal">
    Myrbakkvegen 128, Postboks 71 Kvernvika, 5912 BERGEN<br>
    Phone: 55 83 17 62 | Fax: 55 83 17 69<br>
    Email: post@smilbrink.no
  </address>
</section>

<section class="card card--back-blue" aria-label="Visittkort bakside blå">
  <svg class="emblem" width="124" height="124" viewBox="0 0 124 124" aria-hidden="true">
    <circle cx="62" cy="62" r="56" fill="none" stroke="#ffffff" stroke-width="8"/>
  </svg>
  <p class="back-text">
    Fjellbrinken Tannregulering<br>
    Telefon 55 83 17 62<br>
    www.smilbrink.no
  </p>
</section>

<section class="card card--back-green" aria-label="Visittkort bakside grønn">
  <svg class="emblem" width="124" height="124" viewBox="0 0 124 124" aria-hidden="true">
    <circle cx="62" cy="62" r="56" fill="none" stroke="#ffffff" stroke-width="8"/>
  </svg>
  <p class="back-text">Fjellbrinken Tannregulering | Telefon 55 83 17 62 | www.smilbrink.no</p>
</section>

</body>
</html>
```